Bastion Guard Services

Our Company is a security business which needs a cut edge design, the final product should have all relevant information and maintain a bold but modern and professional look.

Target Market(s)

A cut edge design which will attract any audience

Industry/Entity Type

Security

Contact Information for Business Card

BASTION GUARD SERVICES

Daniel Kowalski
Operations Manager
Phone: 0419 357 216

Email: info@bastionguardex.com.au
Web: www.bastionguardex.com.au

Requirements
Must have
• Must be double sided and contain all relevant information and the company logo.

```html
<!DOCTYPE html>
<html lang="en">
<head>
<meta charset="utf-8">
<title>Bastion Guard Services – Business Card</title>
<link href="https://fonts.googleapis.com/css2?family=Rajdhani:wght@500;600;700&display=swap" rel="stylesheet">
<style>
  :root {
    --bg: #d9dee0;
    --paper: #ffffff;
    --slate: #3d565c;
    --slate-dark: #2f464b;
    --slate-light: #4b666c;
    --ink: #34474c;
    --orange: #f3951f;
    --mist: #c9d3d5;
  }
  * { margin: 0; padding: 0; box-sizing: border-box; }
  html, body {
    width: 1200px; height: 960px; overflow: hidden;
    background: var(--bg);
    font-family: "Rajdhani", "Arial Narrow", sans-serif;
  }
  .canvas {
    width: 1200px; height: 960px;
    display: flex; flex-direction: column; align-items: center; justify-content: center;
    gap: 40px;
  }
  .card {
    position: relative;
    width: 720px; height: 412px;
    overflow: hidden;
    box-shadow: 0 6px 18px rgba(0,0,0,.18);
  }

  /* Front */
  .card-front { background: var(--paper); }
  .brand {
    display: flex; align-items: center; gap: 14px;
  }
  .brand-dot {
    width: 34px; height: 34px; border-radius: 50%;
    background: var(--orange); flex: none;
  }
  .brand-name {
    font-weight: 700; letter-spacing: 2px; text-transform: uppercase;
    line-height: 1;
  }
  .card-front .brand { position: absolute; left: 56px; top: 70px; }
  .card-front .brand-name { font-size: 46px; color: var(--ink); }

  .person { position: absolute; left: 64px; top: 262px; }
  .person-name {
    font-size: 32px; font-weight: 600; letter-spacing: 2px; color: var(--ink);
    text-transform: uppercase;
  }
  .person-role { font-size: 22px; font-weight: 600; color: var(--ink); margin-top: 6px; padding-left: 18px; }

  .contact {
    position: absolute; left: 426px; top: 258px;
    list-style: none; font-size: 19px; font-weight: 600; color: var(--ink);
    line-height: 1.5;
  }
  .contact .phone { font-size: 22px; letter-spacing: 1px; }

  .front-stripe { position: absolute; left: 0; right: 0; bottom: 30px; height: 11px; background: var(--orange); }
  .front-band { position: absolute; left: 0; right: 0; bottom: 0; height: 30px; background: var(--slate); }

  /* Back */
  .card-back {
    background: linear-gradient(135deg, var(--slate-light) 0%, var(--slate) 55%, var(--slate-dark) 100%);
  }
  .card-back .brand {
    position: absolute; left: 0; right: 0; top: 150px; justify-content: center;
  }
  .card-back .brand-name { font-size: 52px; color: var(--mist); }
  .card-back .brand-dot { width: 38px; height: 38px; }

  .web-tab {
    position: absolute; left: 250px; right: 0; bottom: 28px;
    height: 36px; background: var(--orange);
    clip-path: polygon(14px 0, calc(100% - 28px) 0, 100% 100%, 0 100%);
    display: flex; align-items: center; justify-content: center;
    font-size: 19px; font-weight: 700; letter-spacing: 1px; color: var(--slate-dark);
  }
</style>
</head>
<body>
<main class="canvas">
  <section class="card card-front" aria-label="Business card front">
    <div class="brand">
      <span class="brand-dot"></span>
      <span class="brand-name">Bastion Guard</span>
    </div>
    <div class="person">
      <p class="person-name">Daniel Kowalski</p>
      <p class="person-role">Operations Manager</p>
    </div>
    <ul class="contact">
      <li class="phone">0419 357 216</li>
      <li>info@bastionguardex.com.au</li>
      <li>www.bastionguardex.com.au</li>
    </ul>
    <div class="front-stripe"></div>
    <div class="front-band"></div>
  </section>

  <section class="card card-back" aria-label="Business card back">
    <div class="brand">
      <span class="brand-dot"></span>
      <span class="brand-name">Bastion Guard</span>
    </div>
    <div class="web-tab">www.bastionguardex.com.au</div>
  </section>
</main>
</body>
</html>
```